Boutique custom software development company needs new business card

Our nearly 20 year old custom software development company would like to better include the fact that we are now providing Bitcoin services. These new services are B2B include education (how to acquire and securely hold Bitcoin) and integrating Bitcoin payments into existing ecommerce sites or other existing systems. Please keep the card clean and simple. Attached is our current design and some other files. vexalon.example

Target Market(s)

businesses owners interested in long term relationship

Industry/Entity Type

Custom software development and Bitcoin

Contact Information for Business Card

Marcus Ellwood, marcus@vexalon.example, vexalon.example, (888) 555-VEXAL

Font styles to use
Other font styles liked:
• monospace

Requirements
Must have
• double-sided
Nice to have
• clean and simple
Should not have
• physical address

```html
<!DOCTYPE html>
<html lang="en">
<head>
<meta charset="utf-8">
<title>Vexalon Business Card</title>
<link href="https://fonts.googleapis.com/css2?family=IBM+Plex+Mono:wght@500&family=Lato:wght@400&family=Montserrat:wght@500;800&display=swap" rel="stylesheet">
<style>
  :root {
    --backdrop: #cbd3dd;
    --card: #ffffff;
    --brand-blue: #4073b8;
    --brand-orange: #f27e22;
    --ink-grey: #545c63;
    --rule: #5a6168;
  }
  html, body {
    margin: 0;
    padding: 0;
    width: 1200px;
    height: 1200px;
    overflow: hidden;
    background: var(--backdrop);
  }
  .canvas {
    position: relative;
    width: 1200px;
    height: 1200px;
    background: var(--backdrop);
  }
  .card {
    position: absolute;
    left: 319px;
    width: 561px;
    height: 322px;
    background: var(--card);
  }
  .card--front { top: 243px; }
  .card--back { top: 635px; }

  .front-lockup {
    position: absolute;
    left: 0;
    right: 0;
    top: 95px;
    text-align: center;
  }
  .wordmark {
    margin: 0;
    font-family: "Montserrat", sans-serif;
    font-weight: 800;
    font-size: 66px;
    line-height: 1;
    letter-spacing: 2px;
    color: var(--brand-blue);
  }
  .tagline {
    margin: 10px 0 0;
    font-family: "Lato", sans-serif;
    font-weight: 400;
    font-size: 25px;
    letter-spacing: -1.2px;
    color: var(--brand-blue);
  }
  .services {
    margin: 22px 0 0;
    font-family: "IBM Plex Mono", monospace;
    font-weight: 500;
    font-size: 14px;
    letter-spacing: 0.5px;
    color: var(--brand-orange);
  }

  .brand-block {
    position: absolute;
    left: 61px;
    top: 81px;
    width: 130px;
    text-align: center;
  }
  .brand-square {
    display: block;
    width: 130px;
    height: 130px;
    background: var(--brand-blue);
  }
  .brand-site {
    margin: 8px 0 0;
    font-family: "Montserrat", sans-serif;
    font-weight: 500;
    font-size: 15px;
    color: var(--ink-grey);
    white-space: nowrap;
  }
  .divider {
    position: absolute;
    left: 228px;
    top: 37px;
    width: 1px;
    height: 247px;
    background: var(--rule);
  }
  .contact {
    position: absolute;
    left: 266px;
    top: 117px;
    font-family: "Montserrat", sans-serif;
    font-weight: 500;
    line-height: 26px;
  }
  .contact p { margin: 0; white-space: nowrap; }
  .contact__name {
    font-size: 22px;
    color: var(--brand-blue);
  }
  .contact__line {
    font-size: 20px;
    color: var(--ink-grey);
  }
</style>
</head>
<body>
<main class="canvas">
  <section class="card card--front">
    <div class="front-lockup">
      <h1 class="wordmark">VEXALON</h1>
      <p class="tagline">developer of custom applications</p>
      <p class="services">+ bitcoin payments &amp; education</p>
    </div>
  </section>

  <section class="card card--back">
    <div class="brand-block">
      <span class="brand-square"></span>
      <p class="brand-site">vexalon.example</p>
    </div>
    <div class="divider"></div>
    <div class="contact">
      <p class="contact__name">Marcus Ellwood</p>
      <p class="contact__line">marcus@vexalon.example</p>
      <p class="contact__line">(888) 555-VEXAL</p>
    </div>
  </section>
</main>
</body>
</html>
```